Nimbo58.com.au Website and company image design

We are looking for an exceptional website designer / company to work with our new Australian Hosting Company

Nimbo58 is a new Cloud Hosting company launching in Australia that provides Scalable, On Demand computing resources to the Australian Market Place. Scalable, On Demand ocmputing is a nice way of saying fully scalable / redundant Virtual Private Server.

We require a full company image to be developed along with a Logo and Website. There is scope for ongoing development (preferred) for the successful candidate.

Website developement will require extensive jQuery ability (sliders for ordering etc (see: http://www.hostrix-example.com.au/virtual-dedicated-servers/253/zar_vps.html).

Please communicate directly with me to establish full website scope and request further documentation / content.

Target Market(s)

Website Designers, programmers, technicians and large companies

Industry/Entity Type

It Company

Requirements
Must have
• Slider ordering system such as http://www.hostrix-example.com.au/virtual-dedicated-servers/253/zar_vps.html

Nice to have
• CMS backend system
Should not have
• Should NOT be a monster template copy!!!

```html
<!DOCTYPE html>
<html lang="en">
<head>
<meta charset="utf-8">
<title>Nimbo58 – Cloud Hosting Services</title>
<link href="https://fonts.googleapis.com/css2?family=Dosis:wght@300;400;500&family=Lato:ital,wght@0,400;0,700;1,400&display=swap" rel="stylesheet">
<style>
  :root{
    --brand-blue:#1a5fb4;
    --deep-blue:#1d4f9e;
    --link-blue:#2a66c4;
    --sky-top:#cfe3f8;
    --sky-bottom:#e9f2fc;
    --hero-top:#f4f8fe;
    --hero-bottom:#dcebfb;
    --orange:#f26a10;
    --orange-dark:#e05a00;
    --text-dark:#222;
    --text-mid:#555;
    --rule:#dcdcdc;
    --footer-top:#1c1c1c;
    --footer-bottom:#000;
    --footer-text:#e6e6e6;
  }
  *{box-sizing:border-box;margin:0;padding:0}
  html,body{width:875px;height:1200px;overflow:hidden;background:#fff}
  body{position:relative;font-family:"Lato",Arial,sans-serif;color:var(--text-dark)}
  .abs{position:absolute}
  ul{list-style:none}

  /* header */
  .site-header{left:0;top:0;width:875px;height:111px;
    background:linear-gradient(var(--sky-bottom),var(--sky-top));
    border-top:3px solid #3b82d8;border-bottom:1px solid #b7d0ee}
  .header-phone{left:694px;top:0;width:152px;height:35px;background:#fff;
    border-radius:0 0 4px 4px;box-shadow:0 1px 3px rgba(0,0,0,.12);
    display:flex;align-items:center;justify-content:center;gap:6px;
    color:var(--orange);font-size:18px;font-family:"Dosis",sans-serif}
  .brand{left:26px;top:41px;display:flex;align-items:center;gap:6px;
    font-family:"Lato",sans-serif;font-weight:700;font-size:27px;color:var(--brand-blue)}
  .brand-mark{width:16px;height:16px;border-radius:50%;background:var(--brand-blue)}
  .main-nav{top:82px;left:0;width:875px;height:26px}
  .main-nav a{position:absolute;top:0;font-weight:700;font-size:13.5px;color:var(--link-blue);text-decoration:none}
  .nav-pointer{left:397px;top:105px;width:0;height:0;border-left:6px solid transparent;border-right:6px solid transparent;border-bottom:6px solid #fff}

  /* hero */
  .hero{left:0;top:150px;width:875px;height:301px;
    background:linear-gradient(var(--hero-top),var(--hero-bottom))}
  .hero-title{left:40px;top:174px;font-family:"Dosis",sans-serif;font-weight:300;color:var(--deep-blue);line-height:1.05}
  .hero-title .lead{display:block;font-size:31px}
  .hero-title .main{display:block;font-size:33px;margin-top:2px;letter-spacing:.3px}
  .hero-copy{left:41px;top:250px;width:330px;font-size:10.5px;line-height:15.5px;color:var(--brand-blue)}
  .hero-copy p+p{margin-top:5px}
  .btn{top:342px;height:28px;width:105px;border-radius:3px;display:flex;align-items:center;justify-content:center;
    color:#fff;font-size:12.5px;box-shadow:0 6px 6px -3px rgba(120,150,200,.35)}
  .btn-plans{left:40px;background:linear-gradient(#ff7a1e,var(--orange-dark))}
  .btn-more{left:158px;background:linear-gradient(#2b73d2,#1656b0)}
  .hero-art{left:474px;top:158px;width:330px;height:252px;border-radius:40px;
    background:radial-gradient(circle at 35% 30%,#7fb6f0 0,#b9d6f4 35%,rgba(220,235,251,0) 70%)}

  /* domain plans */
  .plan{top:479px;width:160px}
  .plan h3{font-size:13px;font-weight:700;color:var(--link-blue)}
  .plan p{font-size:9.2px;line-height:15px;margin-top:3px}
  .plan ul{margin-top:5px}
  .plan li{font-size:9.2px;line-height:17px;color:#333;padding-left:9px;position:relative}
  .plan li::before{content:"";position:absolute;left:0;top:6px;border-left:3px solid #333;border-top:2.5px solid transparent;border-bottom:2.5px solid transparent}
  .divider{left:23px;top:611px;width:830px;height:1px;background:var(--rule)}

  /* info columns */
  .col-title{top:636px;font-family:"Dosis",sans-serif;font-size:18px;font-weight:400;color:#222}
  .why-photo{left:25px;top:667px;width:234px;height:81px;
    background:linear-gradient(120deg,#3d63a8,#9ab5dd 55%,#e8eef7 70%,#4a70b3)}
  .why-lead{left:25px;top:758px;width:234px;font-size:11.5px;line-height:15px;text-align:justify}
  .why-body{left:25px;top:794px;width:234px;font-size:9.3px;line-height:15.3px;color:var(--text-mid);text-align:justify}
  .why-body p+p{margin-top:4px}
  .feat-lead{left:301px;top:668px;width:240px;font-size:11.5px;line-height:15px}
  .feat-body{left:302px;top:705px;width:236px;font-size:9.3px;line-height:15.3px;color:var(--text-mid);text-align:justify}
  .feat-list{left:308px;top:764px}
  .feat-list li{display:flex;align-items:center;gap:9px;height:22.2px;font-size:10.5px;color:var(--orange)}
  .testimonials{left:577px;top:666px;width:255px}
  .quote{font-style:italic;font-size:9.3px;line-height:15.3px;color:var(--link-blue)}
  .author{font-size:9.5px;font-weight:700;margin:6px 0 12px;color:#111}

  /* footer */
  .site-footer{left:0;top:952px;width:875px;height:248px;
    background:linear-gradient(var(--footer-top),var(--footer-bottom));color:var(--footer-text)}
  .foot-col{top:988px}
  .foot-col h4{font-size:12.5px;font-weight:700;color:#fff;margin-bottom:10px}
  .foot-col li{font-size:10px;line-height:22.3px}
  .support-title{left:633px;top:983px;font-family:"Dosis",sans-serif;font-size:20px;color:#fff}
  .support-phone{left:636px;top:1016px;display:flex;align-items:center;gap:13px;font-family:"Dosis",sans-serif;font-size:21px;color:var(--orange)}
  .support-mail{left:636px;top:1050px;display:flex;align-items:center;gap:13px;font-size:13px;color:var(--orange)}
  .foot-rule{left:26px;top:1145px;width:817px;height:1px;background:#3a3a3a}
  .copyright{left:28px;top:1171px;font-size:10px;color:#ddd}
</style>
</head>
<body>

<header class="site-header abs"></header>
<div class="header-phone abs">
  <svg width="10" height="16" viewBox="0 0 10 16"><path d="M3 1 C0 3 0 13 3 15 L5 13 C3 11 3 5 5 3 Z" fill="var(--orange)"/></svg>
  555 014 2290
</div>
<div class="brand abs"><span class="brand-mark"></span>Nimbo58</div>
<nav class="main-nav abs">
  <a style="left:389px">Main</a>
  <a style="left:452px">About Us</a>
  <a style="left:539px">Services</a>
  <a style="left:623px">Hosting</a>
  <a style="left:701px">Support</a>
  <a style="left:780px">Contact</a>
</nav>
<div class="nav-pointer abs"></div>

<section class="hero abs"></section>
<h1 class="hero-title abs"><span class="lead">We Provide Subperb</span><span class="main">CLOUDS HOSTING SERVICES</span></h1>
<div class="hero-copy abs">
  <p>Lorem ipsum dolor sit amet, consectetuer adipiscing elit. Nam cursus. Morbi ut mi. Nullam enim leo, egestas id, condimentum at, laoreet mattis, massa.</p>
  <p>Sed eleifend nonummy diam. Praesent mauris ante, elementum et, bibendum at, posuere sit amet.</p>
</div>
<a class="btn btn-plans abs">View Plans</a>
<a class="btn btn-more abs">Learn More</a>
<div class="hero-art abs" role="img" aria-label="Illustration of a blue cloud with an orange firewall connected to servers, desktop computers and a laptop"></div>

<div class="plan abs" style="left:24px"><h3>Domain Name</h3><p>Lorem ipsum dolor sit amet, conse ctetuer adipiscing elit.</p><ul><li>Domain Featued First here</li><li>Domain Featued second here</li><li>Domain Third Feature</li></ul></div>
<div class="plan abs" style="left:200px"><h3>Domain Name</h3><p>Lorem ipsum dolor sit amet, conse ctetuer adipiscing elit.</p><ul><li>Domain Featued First here</li><li>Domain Featued second here</li><li>Domain Third Feature</li></ul></div>
<div class="plan abs" style="left:367px"><h3>Domain Name</h3><p>Lorem ipsum dolor sit amet, conse ctetuer adipiscing elit.</p><ul><li>Domain Featued First here</li><li>Domain Featued second here</li><li>Domain Third Feature</li></ul></div>
<div class="plan abs" style="left:536px"><h3>Domain Name</h3><p>Lorem ipsum dolor sit amet, conse ctetuer adipiscing elit.</p><ul><li>Domain Featued First here</li><li>Domain Featued second here</li><li>Domain Third Feature</li></ul></div>
<div class="plan abs" style="left:704px"><h3>Domain Name</h3><p>Lorem ipsum dolor sit amet, conse ctetuer adipiscing elit.</p><ul><li>Domain Featued First here</li><li>Domain Featued second here</li><li>Domain Third Feature</li></ul></div>
<div class="divider abs"></div>

<h2 class="col-title abs" style="left:25px">Why Our Hosting</h2>
<div class="why-photo abs" role="img" aria-label="Photo of a businesswoman holding a laptop against a glass office building"></div>
<p class="why-lead abs">Lorem ipsum dolor sit amet, consectetuer adipiscing elit. Nam cursus. Morbi ut mi.</p>
<div class="why-body abs">
  <p>Nullam enim leo, egestas id, condimentum at, laoreet mattis, massa. Sed eleifend nonummy diam.</p>
  <p>Praesent mauris ante, elementum et, bibendum at, posuere sit amet, nibh. Duis tincidunt lectus quis dui viverra vestibulum. Suspendisse vulputate aliquam dui. Nulla elementum dui ut augue. Aliquam vehicula mi at mauris. Maecenas placerat</p>
</div>

<h2 class="col-title abs" style="left:297px">Featured Services</h2>
<p class="feat-lead abs">Lorem ipsum dolor sit amet, consectetuer adipi scing elit. Nam cursus. Morbi ut mi.</p>
<p class="feat-body abs">Duis tincidunt lectus quis dui viverra vestibulum. Suspendisse vulputate aliquam dui. Nulla elementum dui ut augue.</p>
<ul class="feat-list abs">
  <li><svg width="13" height="12" viewBox="0 0 13 12"><path d="M1 6 L5 10 L12 1" stroke="var(--orange)" stroke-width="2.4" fill="none"/></svg>First Hosting Services Including Service</li>
  <li><svg width="13" height="12" viewBox="0 0 13 12"><path d="M1 6 L5 10 L12 1" stroke="var(--orange)" stroke-width="2.4" fill="none"/></svg>Your Secon Hosting Services Including Service</li>
  <li><svg width="13" height="12" viewBox="0 0 13 12"><path d="M1 6 L5 10 L12 1" stroke="var(--orange)" stroke-width="2.4" fill="none"/></svg>Third Hosting Services Including Service</li>
  <li><svg width="13" height="12" viewBox="0 0 13 12"><path d="M1 6 L5 10 L12 1" stroke="var(--orange)" stroke-width="2.4" fill="none"/></svg>Fouth Hosting Services Including Service</li>
  <li><svg width="13" height="12" viewBox="0 0 13 12"><path d="M1 6 L5 10 L12 1" stroke="var(--orange)" stroke-width="2.4" fill="none"/></svg>Fifth Hosting Including Service</li>
  <li><svg width="13" height="12" viewBox="0 0 13 12"><path d="M1 6 L5 10 L12 1" stroke="var(--orange)" stroke-width="2.4" fill="none"/></svg>More Featured Services</li>
</ul>

<h2 class="col-title abs" style="left:574px">Customer Testimonials</h2>
<div class="testimonials abs" style="top:666px">
  <p class="quote">Lorem ipsum dolor sit amet, consectetuer adipiscing elit. Nam cursus. Morbi ut mi. Nullam enim leo, egestas id, condimentum at, laoreet mattis, massa. Sed eleifend nonummy diam.</p>
  <p class="author">By Author Name</p>
  <p class="quote">Lorem ipsum dolor sit amet, consectetuer adipiscing elit. Nam cursus. Morbi ut mi. Nullam enim leo, egestas id, condimentum at, laoreet mattis, massa. Sed eleifend nonummy diam.</p>
  <p class="author">By Author Name</p>
  <p class="quote">Lorem ipsum dolor sit amet, consectetuer adipiscing elit. Nam cursus. Morbi ut mi. Nullam enim leo, egestas id, condimentum at, laoreet mattis, massa. Sed eleifend nonummy diam.</p>
  <p class="author">By Author Name</p>
</div>

<footer class="site-footer abs"></footer>
<div class="foot-col abs" style="left:37px"><h4>Company</h4><ul><li>Home</li><li>About Our Company</li><li>Why We Are</li><li>Our Services</li></ul></div>
<div class="foot-col abs" style="left:172px"><h4>Our Hostings</h4><ul><li>Recent Blog</li><li>Customer Testimonials</li><li>Hosting Plans</li><li>Hosting Services</li></ul></div>
<div class="foot-col abs" style="left:325px"><h4>Support &amp; Services</h4><ul><li>Support</li><li>FAQ</li><li>Customer Services</li><li>Order Now</li></ul></div>
<div class="foot-col abs" style="left:485px"><h4>Contact Info</h4><ul><li>Term of Uses</li><li>Privacy Policy</li><li>Contact Info</li></ul></div>
<h3 class="support-title abs">Customer Support 24/7</h3>
<div class="support-phone abs">
  <svg width="22" height="26" viewBox="0 0 22 26"><path d="M5 1 L9 7 L6 10 C7 14 10 18 14 20 L17 17 L21 22 L17 25 C9 24 2 14 1 5 Z" fill="#fff"/></svg>
  555 014 2290
</div>
<div class="support-mail abs">
  <svg width="26" height="18" viewBox="0 0 26 18"><rect x="0" y="0" width="26" height="18" rx="2" fill="#fff"/><path d="M1 1 L13 10 L25 1" stroke="#111" stroke-width="1.6" fill="none"/></svg>
  support@nimbo58mail.com
</div>
<div class="foot-rule abs"></div>
<p class="copyright abs">© 2012 Company Name &nbsp;|&nbsp; All right reserved</p>

</body>
</html>
```